Consulting/Brand Licensing business needs business card

We need a business card created for our IP company, that also does consulting and brand licensing. We would like this card to be vague, as our other business' are in the cannabis industry and this is a non-cannabis touching entity. Perhaps something that hints vaguely at the industry without alerting or possibly offending the receiver.

Target Market(s)

CEOs/Key Decision Makers/Industry Leaders

Contact Information for Business Card

No address, simply list Seattle, WA. Phone: 206-555-0147. Name: Dilan Vesterby // email: Dilan@pulvanixa.com

Colors

Designer to choose colors to be used in the design.

Requirements
Must have
• Logo, Name, Email, Phone number, "Consulting, Licensing and Branding Specialists"
Nice to have
• We would like this to be more professional than playful.

```html
<!DOCTYPE html>
<html lang="en">
<head>
<meta charset="utf-8">
<title>Pulvanixa business card</title>
<link href="https://fonts.googleapis.com/css2?family=Questrial&family=Montserrat:wght@600&display=swap" rel="stylesheet">
<style>
  :root {
    --backdrop: #2b2b2c;
    --card: #f7f7f6;
    --accent: #e2572f;
    --ink: #444446;
    --ghost: #e4e4e4;
  }
  html, body {
    margin: 0;
    width: 1200px;
    height: 900px;
    overflow: hidden;
    background: var(--backdrop);
  }
  .stage {
    position: relative;
    width: 1200px;
    height: 900px;
  }
  .card {
    position: absolute;
    width: 620px;
    height: 354px;
    background: var(--card);
    border-radius: 28px;
    overflow: hidden;
    box-shadow: 0 14px 30px rgba(0,0,0,.45);
    font-family: "Questrial", sans-serif;
  }
  .card--front { left: 90px; top: 70px; }
  .card--back  { left: 490px; top: 476px; }

  .brand-name {
    margin: 0;
    color: var(--accent);
    font-family: "Questrial", sans-serif;
    font-weight: 400;
    letter-spacing: .5px;
    white-space: nowrap;
  }
  .card--front .brand-name {
    position: absolute;
    left: 0; right: 0;
    top: 148px;
    text-align: center;
    font-size: 46px;
  }
  .card--back .brand-name {
    position: absolute;
    left: 40px;
    top: 46px;
    font-size: 38px;
  }

  .brand-ghost {
    position: absolute;
    right: -78px;
    top: 150px;
    transform: rotate(90deg);
    font-family: "Questrial", sans-serif;
    font-size: 88px;
    color: var(--ghost);
    white-space: nowrap;
  }

  .holder-name {
    position: absolute;
    left: 40px;
    bottom: 86px;
    margin: 0;
    font-family: "Montserrat", sans-serif;
    font-weight: 600;
    font-size: 19px;
    letter-spacing: .5px;
    text-transform: uppercase;
    color: var(--accent);
  }
  .rule {
    position: absolute;
    left: 40px;
    right: 40px;
    bottom: 72px;
    height: 1.5px;
    background: var(--accent);
  }
  .contact {
    position: absolute;
    left: 40px;
    bottom: 40px;
    margin: 0;
    font-size: 15px;
    color: var(--ink);
    white-space: nowrap;
  }
  .contact .label, .contact .sep { color: var(--accent); }
  .contact .sep { margin: 0 7px; }
</style>
</head>
<body>
<main class="stage">
  <section class="card card--front" aria-label="Card front">
    <p class="brand-name">Pulvanixa, Inc</p>
  </section>

  <section class="card card--back" aria-label="Card back">
    <span class="brand-ghost" aria-hidden="true">Pulvanixa</span>
    <p class="brand-name">Pulvanixa, Inc</p>
    <h1 class="holder-name">Dilan Vesterby</h1>
    <div class="rule"></div>
    <p class="contact">
      <span class="label">T.</span> 206-555-0147<span class="sep">|</span><span class="label">E.</span> Dilan@pulvanixa.com<span class="sep">|</span>simply list Seattle, WA
    </p>
  </section>
</main>
</body>
</html>
```